Business Card Design

We need a business card designed to portray the message that we are wedding and event stylists. We set up garden ceremonies and style wedding reception venues with chair covers and sashes, backdrops and draping's, wishing wells, tealight holders, table centerpieces. We also style corporate functions - Christmas parties, gala dinners, school formals, award nights. The colour of our uniforms are black and hot pink, if these colours could be incorporated. We would like to be able to use this design for letterhead, flyers and postcards etc. We would like the design to portray a professional, classic image that would relate to both spectrums of our business, weddings and corporate events. If you could develop a logo to incorporate would be great

Target Market(s)

brides, corporate compaines

Industry/Entity Type

Wedding

Contact Information for Business Card

Velvet Aisle & Function Rentals
Phone: 0413 586 190 Email:vaafr@quokkamail.com
Web: www.velvetaisleandfunctions.com.au

Requirements
Must have
• Must include that we set up for weddings, engagements, birthdays, anniversaries, corporate functions, school formals, any occasion.

```html
<!DOCTYPE html>
<html lang="en">
<head>
<meta charset="utf-8">
<title>Velvet Aisle &amp; Function Rentals – Business Card</title>
<link rel="stylesheet" href="https://fonts.googleapis.com/css2?family=Tinos:ital,wght@0,400;1,400&display=swap">
<style>
  :root {
    --page-bg: #f4eef5;
    --card-black: #000000;
    --ornament-pink: #b24fc4;
    --ornament-deep: #5a1f66;
    --frame-pink: #c25ad3;
    --text-white: #ffffff;
  }
  html, body {
    margin: 0;
    width: 1200px;
    height: 1000px;
    overflow: hidden;
    background: var(--page-bg);
  }
  .canvas {
    position: relative;
    width: 1200px;
    height: 1000px;
  }
  .business-card {
    position: absolute;
    left: 61px;
    top: 174px;
    width: 1078px;
    height: 651px;
    border-radius: 22px;
    background: var(--card-black);
    overflow: hidden;
    font-family: "Tinos", "Times New Roman", serif;
    color: var(--text-white);
  }
  .ornament-art {
    position: absolute;
    left: 30px;
    top: 45px;
    width: 570px;
    height: 540px;
  }
  .brand-sign {
    position: absolute;
    left: 155px;
    top: 190px;
    width: 313px;
    height: 185px;
    box-sizing: border-box;
    border: 7px solid var(--frame-pink);
    background: var(--card-black);
    display: flex;
    align-items: center;
    justify-content: center;
    text-align: center;
  }
  .brand-name {
    margin: 0;
    font-size: 36px;
    font-weight: 400;
    line-height: 1.35;
  }
  .services {
    position: absolute;
    left: 588px;
    top: 75px;
    margin: 0;
    padding: 0;
    list-style: none;
    font-size: 37px;
    font-style: italic;
    line-height: 50px;
  }
  .services li::before {
    content: "\2666\00a0";
    font-style: normal;
    font-size: 30px;
  }
  .contact {
    position: absolute;
    left: 470px;
    top: 486px;
    width: 560px;
    margin: 0;
    text-align: center;
    font-size: 27px;
    font-style: italic;
    line-height: 33px;
  }
</style>
</head>
<body>
<div class="canvas">
  <section class="business-card">
    <svg class="ornament-art" viewBox="0 0 570 540" role="img" aria-label="Ornate hot pink Victorian sign frame with arch, finials, griffins, ivy garland and wreath">
      <defs>
        <radialGradient id="ornamentGlow" cx="50%" cy="50%" r="60%">
          <stop offset="0%" stop-color="var(--ornament-pink)"/>
          <stop offset="70%" stop-color="var(--ornament-deep)"/>
          <stop offset="100%" stop-color="var(--card-black)"/>
        </radialGradient>
      </defs>
      <rect x="0" y="0" width="570" height="540" rx="40" fill="url(#ornamentGlow)"/>
    </svg>
    <div class="brand-sign">
      <h1 class="brand-name">Velvet Aisle<br>&amp;<br>Function Rentals</h1>
    </div>
    <ul class="services">
      <li>Birthdays</li>
      <li>Weddings</li>
      <li>Engagements</li>
      <li>Anniversaries</li>
      <li>School Formals</li>
      <li>Corporate Functions</li>
      <li>Any occasion big or small</li>
    </ul>
    <p class="contact">
      Phone: 0413 586 190<br>
      Email:vaafr@quokkamail.com<br>
      Web: www.velvetaisleandfunctions.com.au
    </p>
  </section>
</div>
</body>
</html>
```